Stationery Design Project - Mark Delaveri

I have recently designed my personal logo - Mark Delaveri (here on pixelhive.com) and now i'm looking to complete my corporate identity, with adding:
- Business Card
- Letter Head
- Envelope
- Brochure template (that will be used to promote any of the workshops or other services I provide along with a short summary about my credentials, and testimonials) - you can take your pick from the website: http://markdelaveri.com

Refer to website for more insight into the brand and the look & feel

PS.
- PLEASE REFER TO ATTACHED FILE AND READ THE "SHOULD NOT HAVE SECTION OF THIS BRIEF"
- I have attached two vector files, displaying the logo alteration on two different backgrounds (dark & light)
Updates

ONLY 2 DAYS LEFT ON DEADLINE. KEEP THOSE DESIGNS COMING.

Target Market(s)

1) One-on-one Business Executive 2) Companies requesting my workshops for mid management teams & public speaking events like BRIM Forums

Industry/Entity Type

Business

Requirements
Must have
• - must fit the look and feel of the logo (notice that I have attached the logo, and an emblem)
- the final files should be ready for printing - with info on colours, sizes, bleed area, margins, UV spot (if applicable), suggested material to print on (applies to business cards in particular)
- brand guide lines should be laid out too (font, colour, etc ...)
Nice to have
• It would be nice to produce something different that your standard sizes & di-cut in terms of business card, and letter head ...
Should not have
• THE EMBLEM (MD) AND THE LOGO (MARK DELAVERI) SHOULD NOT BE LAYED OUT AS PER THE ATTACHED FILE - THEY SHOULD BE SEPARATED - THE EMBLEM (MD) CAN BE USED IN PARTIAL OR AS WATERMARK - BUT NOT THE LOGO (MARK DELAVERI)

```html
<!DOCTYPE html>
<html lang="en">
<head>
<meta charset="utf-8">
<title>Office Element – Business Card</title>
<link href="https://fonts.googleapis.com/css2?family=Questrial&display=swap" rel="stylesheet">
<style>
  :root {
    --ink: #23232e;
    --paper: #ffffff;
    --brown: #3a3030;
    --rule: #c9c9cf;
    --accent: #3ab4e6;
    --grey-text: #555559;
    --card-text: #b4b4ba;
    --stage-light: #f4f4f4;
    --stage-dark: #b3b3b3;
  }
  * { margin: 0; padding: 0; box-sizing: border-box; }
  html, body { width: 1200px; height: 842px; overflow: hidden; background: var(--paper); }
  body { position: relative; font-family: "Questrial", "Century Gothic", sans-serif; color: var(--ink); }

  .header-band { position: absolute; left: 16px; top: 0; width: 1184px; height: 233px; background: var(--ink); }
  .header-rule { position: absolute; left: 16px; top: 101px; width: 1184px; height: 1px; background: var(--rule); }
  .page-marker { position: absolute; left: 541px; top: 91px; width: 16px; height: 10px; background: var(--accent); }
  .page-number { position: absolute; left: 541px; top: 102px; font-size: 11px; color: var(--rule); }
  .section-label { position: absolute; left: 1018px; top: 50px; font-size: 19px; line-height: 18px; color: var(--paper); letter-spacing: 0.5px; }
  .page-title { position: absolute; left: 135px; top: 148px; font-size: 42px; color: var(--paper); letter-spacing: 1.5px; font-weight: 400; }

  .stage { position: absolute; left: 16px; top: 233px; width: 1184px; height: 525px;
    background: radial-gradient(ellipse 70% 80% at 50% 30%, var(--stage-light) 0%, #dcdcdc 50%, var(--stage-dark) 100%); }

  .card { position: absolute; top: 392px; width: 362px; height: 187px; }
  .card-front { left: 135px; background: var(--paper); border: 1px solid #d0d0d0; }
  .card-back { left: 519px; background: var(--ink); }

  .wordmark { position: absolute; left: 27px; top: 88px; font-size: 29px; color: var(--grey-text); letter-spacing: 0.5px; white-space: nowrap; }

  .company-address { position: absolute; left: 27px; top: 117px; font-size: 8.5px; line-height: 10.5px; color: var(--card-text); }
  .contact-row { position: absolute; left: 14px; top: 152px; display: flex; align-items: center; font-size: 10px; color: var(--paper); white-space: nowrap; }
  .contact-row svg { width: 11px; height: 11px; margin-right: 5px; fill: var(--paper); }
  .contact-row .sep { margin: 0 8px; color: var(--card-text); }

  .size-note { position: absolute; left: 296px; top: 590px; font-size: 16px; color: var(--ink); }
  .callouts { position: absolute; left: 0; top: 0; }
  .uv-label { position: absolute; left: 755px; top: 629px; font-size: 16px; color: var(--ink); }

  .spec-heading { position: absolute; left: 944px; font-size: 17px; color: var(--ink); letter-spacing: 0.5px; }
  .swatch { position: absolute; left: 944px; width: 200px; height: 19px; padding-left: 28px; font-size: 15px; line-height: 19px; }
  .swatch-white { top: 356px; background: var(--paper); color: var(--ink); }
  .swatch-brown { top: 397px; background: var(--brown); color: var(--paper); }
  .swatch-ink { top: 433px; background: var(--ink); color: var(--paper); }

  .footer-band { position: absolute; left: 16px; top: 758px; width: 1184px; height: 84px; background: var(--ink); }
  .footer-wordmark { position: absolute; left: 943px; top: 781px; font-size: 32px; color: var(--paper); letter-spacing: 0.5px; white-space: nowrap; }
</style>
</head>
<body>
  <div class="header-band"></div>
  <div class="header-rule"></div>
  <div class="page-marker"></div>
  <div class="page-number">01</div>
  <div class="section-label">Office<br>Element</div>
  <h1 class="page-title">Business Card</h1>

  <div class="stage"></div>

  <div class="card card-front">
    <div class="wordmark">MARK DELAVERI</div>
  </div>

  <div class="card card-back">
    <div class="company-address">
      Lumera Textiles Co.,Ltd .Westbury<br>
      No.12 3F,Harbor House,Kestrel Lane,Oakfield District,Westbury City,<br>
      Northvale Prov.Country 204000
    </div>
    <div class="contact-row">
      <svg viewBox="0 0 24 24" aria-hidden="true"><path d="M6.6 10.8a15.1 15.1 0 0 0 6.6 6.6l2.2-2.2c.3-.3.7-.4 1-.2 1.1.4 2.3.6 3.6.6.6 0 1 .4 1 1V20c0 .6-.4 1-1 1A17 17 0 0 1 3 4c0-.6.4-1 1-1h3.5c.6 0 1 .4 1 1 0 1.3.2 2.5.6 3.6.1.3 0 .7-.2 1z"/></svg>
      <span>0123-45678901</span>
      <span class="sep">/</span>
      <svg viewBox="0 0 24 24" aria-hidden="true"><path d="M7 2h9l4 4v13H7zM9 4v13h9V7h-3V4zM4 6h2v15h11v2H4z"/></svg>
      <span>0123-45678901</span>
      <span class="sep">/</span>
      <svg viewBox="0 0 24 24" aria-hidden="true"><path d="M2 5h20v14H2zM4 7v.5l8 5.5 8-5.5V7zm0 2.9V17h16V9.9l-8 5.5z"/></svg>
      <span>hello@lumeramail.com</span>
    </div>
  </div>

  <div class="size-note">89*46mm</div>

  <svg class="callouts" width="1200" height="842" aria-hidden="true">
    <polyline points="215,520 215,638 748,638" fill="none" stroke="var(--ink)" stroke-width="1"/>
    <line x1="598" y1="535" x2="598" y2="638" stroke="var(--accent)" stroke-width="1"/>
  </svg>
  <div class="uv-label">UV</div>

  <div class="spec-heading" style="top:321px;">COLOR :</div>
  <div class="swatch swatch-white">C:0 M:0 Y:0 K:0</div>
  <div class="swatch swatch-brown">C:0 M:0 Y:0 K:100</div>
  <div class="swatch swatch-ink">C:0 M:0 Y:0 K:100</div>
  <div class="spec-heading" style="top:561px;">FONT : century gothic</div>

  <div class="footer-band"></div>
  <div class="footer-wordmark">MARK DELAVERI</div>
</body>
</html>
```